Website Design for Professional Services Company

• Create a new website design that is easy to maintain inside of WordPress with a main page design, a design for generic content pages, and a design for customer case studies. Our current design relies on a number of plugins to function, and we would like to get away from that as much as possible. Our current design also requires a fair amount of coding that we would like to get away from. The more we can use native WordPress the better. We are not opposed to a small subset of plugins that are widely used and readily updated. Our current website can be found at https://brindlecrestconsulting.com/. Our fonts (for use in graphics, we don’t want custom fonts on the website itself to make sure it always displays correctly) and colors are as follows:
o Brindlecrest Blue:
 #1b75bc
o Brindlecrest Grey:
 #6d6f71
o Main Font:
 Telegrafico
o Accent Font:
 Nexa Light

```html
<!DOCTYPE html>
<html lang="en">
<head>
<meta charset="utf-8">
<title>Brindlecrest Consulting</title>
<link href="https://fonts.googleapis.com/css2?family=Poppins:wght@300;400;500;600;700&family=Open+Sans:wght@400;600&display=swap" rel="stylesheet">
<style>
:root{
  --blue:#1b75bc;
  --blue-bright:#2a83d6;
  --blue-deep:#0f4f92;
  --grey:#6d6f71;
  --ink:#222;
  --navy:#0b1f3d;
  --card-dark:#2d3142;
  --white:#fff;
}
*{margin:0;padding:0;box-sizing:border-box}
html,body{width:1200px;height:4988px;overflow:hidden}
body{position:relative;background:var(--white);font-family:"Open Sans",sans-serif;color:var(--ink)}
.abs{position:absolute}
.band{position:absolute;left:0;width:1200px;display:block}

/* buttons */
.btn{position:absolute;display:flex;align-items:center;justify-content:center;font-family:"Poppins",sans-serif;font-weight:600;color:var(--white);text-transform:uppercase;letter-spacing:.3px}
.btn::before{content:"";position:absolute;top:0;bottom:0;right:0;left:-8px;background:var(--grey);clip-path:polygon(12% 0,100% 0,100% 100%,12% 100%,0 50%);z-index:0}
.btn::after{content:"";position:absolute;inset:0;background:var(--blue);clip-path:polygon(10% 0,90% 0,100% 50%,90% 100%,10% 100%,0 50%);z-index:1}
.btn span{position:relative;z-index:2}

/* top bar + header */
.topbar-text{left:329px;top:10px;font-size:13px;color:var(--white);font-family:"Poppins",sans-serif}
.social-top{top:6px;width:24px;height:24px;border:1.5px solid var(--white);border-radius:50%}
.brand{font-family:"Poppins",sans-serif;font-weight:600;color:var(--blue);letter-spacing:1px}
.nav a{position:absolute;top:66px;font-family:"Poppins",sans-serif;font-size:17px;color:#333;text-decoration:none}
.nav a.active{color:var(--blue)}

/* hero */
.hero-title{left:143px;top:240px;font-family:"Poppins",sans-serif;font-weight:300;font-size:40px;line-height:45px;color:var(--white)}
.hero-title b{font-weight:600}
.hero-lead{left:143px;top:390px;width:440px;font-size:16px;line-height:25px;color:var(--white)}
.dot{top:583px;width:14px;height:14px;border:1.5px solid var(--white);border-radius:50%}
.dot.on{background:var(--white)}

/* why choose */
.why-title{left:143px;top:886px;font-family:"Poppins",sans-serif;font-size:40px;font-weight:400;color:#222}
.why-title b{font-weight:600}
.why-rule{left:143px;top:946px;width:168px;height:3px;background:var(--grey)}
.why-text{left:143px;top:978px;width:430px;font-size:14.5px;line-height:25px;color:#333}
.why-art{left:694px;top:862px;width:350px;height:404px;border-radius:24px;background:radial-gradient(circle at 40% 30%,#4aa0e6 0%,transparent 45%),radial-gradient(circle at 75% 75%,#2f86d0 0%,transparent 40%),linear-gradient(160deg,#0e2d52,#1b75bc 55%,#0a1e38)}
.why-shadow{left:650px;top:1262px;width:440px;height:26px;border-radius:50%;background:radial-gradient(#bbb,transparent 70%)}

/* section titles */
.section-title{position:absolute;left:0;width:1200px;text-align:center;font-family:"Poppins",sans-serif}
.divider{position:absolute;left:555px;width:90px;height:14px}

/* services */
.svc-card{position:absolute;top:1563px;width:240px;height:424px;background:var(--white);clip-path:polygon(50% 0,100% 15%,100% 86%,50% 100%,0 86%,0 15%)}
.svc-img{position:absolute;left:8px;top:8px;width:224px;height:238px;clip-path:polygon(50% 0,100% 14%,100% 100%,0 100%,0 14%)}
.svc-icon{position:absolute;left:91px;top:199px;width:58px;height:58px;border-radius:50%;background:var(--white);border:2px solid var(--blue);display:flex;align-items:center;justify-content:center}
.svc-card h3{position:absolute;left:0;top:270px;width:240px;text-align:center;font-family:"Poppins",sans-serif;font-size:14px;font-weight:600;color:#222}
.svc-card p{position:absolute;left:14px;top:296px;width:212px;text-align:center;font-size:12.5px;line-height:21px;color:#555}
.svc-arrow{position:absolute;left:106px;top:382px;width:28px;height:28px;border-radius:50%;background:var(--blue);display:flex;align-items:center;justify-content:center}
.join-circle{left:565px;top:2051px;width:70px;height:70px;border-radius:50%;background:var(--blue);border:5px solid var(--white)}

/* core values */
.values-title{top:2172px;font-size:38px;line-height:49px;font-weight:500;color:#222}
.values-rule{left:528px;top:2284px;width:144px;height:3px;background:var(--blue)}
.value{position:absolute;width:230px}
.value h4{font-family:"Poppins",sans-serif;font-size:21px;font-weight:500;color:#222;line-height:30px}
.value p{font-size:14.5px;line-height:22px;color:#444}
.value.left{text-align:right}
.value-icon{position:absolute;width:60px;height:60px}
.core-ring{left:461px;top:2338px;width:278px;height:278px}
.core-disc{left:484px;top:2361px;width:232px;height:232px;border-radius:50%;background:#f3f4f6;box-shadow:0 0 0 1px #e3e4e6;display:flex;align-items:center;justify-content:center;font-family:"Poppins",sans-serif;font-weight:600;font-size:22px;letter-spacing:1px;color:var(--blue)}

/* case studies */
.case-card{position:absolute;top:2860px;width:360px;height:385px;background:var(--card-dark);border-radius:3px}
.case-img{position:absolute;left:13px;top:13px;width:334px;height:200px}
.case-card h3{position:absolute;left:27px;top:234px;font-family:"Poppins",sans-serif;font-size:14px;font-weight:600;color:var(--white)}
.case-card p{position:absolute;left:27px;top:262px;width:310px;font-size:13px;line-height:22px;color:#dfe3ea}
.case-card .btn{left:130px;top:324px;width:106px;height:30px;font-size:10px}

/* blog */
.blog-title{top:3448px;font-size:40px;font-weight:600;color:#222}
.blog-card{position:absolute;top:3570px;width:287px;height:445px;background:var(--white);border:1px solid #e1e1e1;box-shadow:0 2px 6px rgba(0,0,0,.08)}
.blog-img{position:absolute;left:0;top:0;width:285px;height:246px}
.blog-body{position:absolute;left:12px;top:184px;width:261px;height:255px;background:var(--white)}
.blog-date{position:absolute;left:222px;top:10px;width:54px;height:54px;border-radius:50%;background:var(--blue);color:var(--white);font-family:"Poppins",sans-serif;font-size:10.5px;font-weight:600;line-height:13px;text-align:center;padding-top:14px}
.blog-body h3{position:absolute;left:25px;top:28px;width:215px;font-family:"Poppins",sans-serif;font-size:13px;line-height:20px;font-weight:600;color:#222;text-transform:uppercase}
.blog-author{position:absolute;left:25px;top:84px;font-size:13px;font-style:italic;font-weight:600;color:#333}
.blog-author::before{content:"";display:inline-block;width:9px;height:10px;margin-right:7px;background:var(--blue);border-radius:5px 5px 2px 2px}
.blog-body p{position:absolute;left:25px;top:108px;width:225px;font-size:13.5px;line-height:21px;color:#444}
.blog-body .btn{left:35px;top:195px;width:117px;height:30px;font-size:11px}

/* quotation */
.quote-title{left:142px;top:4268px;font-family:"Poppins",sans-serif;font-size:40px;font-weight:400;color:var(--white)}
.quote-text{left:142px;top:4340px;width:470px;font-size:17px;line-height:26px;color:var(--white)}

/* footer */
.footer{left:0;top:4576px;width:1200px;height:349px;background:var(--navy)}
.foot-brand{left:140px;top:4760px;font-size:30px;letter-spacing:2px}
.foot-sub{left:182px;top:4800px;font-family:"Poppins",sans-serif;font-size:11px;letter-spacing:3px;color:#9fb6d3}
.social-foot{top:4828px;width:32px;height:32px;border:1.5px solid var(--white);border-radius:50%}
.foot-h{font-family:"Poppins",sans-serif;font-weight:600;font-size:17px;color:var(--white);letter-spacing:.5px}
.foot-links a{position:absolute;left:482px;font-family:"Poppins",sans-serif;font-size:16.5px;color:#dde6f2;text-decoration:none}
.foot-note{left:755px;top:4686px;width:320px;font-size:13px;line-height:24px;color:#b9c7da}
.foot-input{left:755px;top:4754px;width:302px;height:37px;background:var(--white);border-radius:2px;font-size:13px;color:#555;padding:10px 16px}
.copyright{left:0;top:4925px;width:1200px;height:63px;background:#1b5ea8;color:#e9f0f9;font-size:14px;text-align:center;line-height:63px}
</style>
</head>
<body>

<!-- top bar -->
<svg class="band" style="top:0;height:38px" viewBox="0 0 1200 38"><polygon points="300,0 1200,0 1200,38 270,38" fill="#1b75bc"/></svg>
<div class="abs topbar-text">Need Help? Talk to an Expert 888-555-0142</div>
<div class="abs social-top" style="left:1046px"></div>
<div class="abs social-top" style="left:1078px"></div>

<!-- header -->
<div class="abs brand" style="left:90px;top:72px;font-size:24px">BRINDLECREST</div>
<nav class="nav">
  <a class="active" style="left:433px">Home</a>
  <a style="left:511px">About us</a>
  <a style="left:615px">Services</a>
  <a style="left:712px">Blog</a>
  <a style="left:776px">Case Studies ⌄</a>
</nav>
<div class="btn" style="left:933px;top:58px;width:137px;height:39px;font-size:13px"><span>Get Started</span></div>

<!-- hero -->
<svg class="band" style="top:116px;height:710px" viewBox="0 0 1200 710" role="img" aria-label="Consultant's hands holding a glowing network globe over digital data graphics">
  <defs>
    <linearGradient id="heroBase" x1="0" y1="0" x2="1" y2="0.3">
      <stop offset="0" stop-color="#05080e"/><stop offset=".38" stop-color="#0d1b2e"/><stop offset=".62" stop-color="#173f6c"/><stop offset=".82" stop-color="#2466a3"/><stop offset="1" stop-color="#0c2340"/>
    </linearGradient>
    <radialGradient id="heroGlow" cx=".72" cy=".42" r=".32"><stop offset="0" stop-color="#8ec8ff" stop-opacity=".55"/><stop offset="1" stop-color="#8ec8ff" stop-opacity="0"/></radialGradient>
    <radialGradient id="heroWarm" cx=".9" cy=".72" r=".2"><stop offset="0" stop-color="#f0a040" stop-opacity=".35"/><stop offset="1" stop-color="#f0a040" stop-opacity="0"/></radialGradient>
  </defs>
  <polygon points="0,0 1200,0 1200,594 600,710 0,594" fill="#1b75bc"/>
  <polygon points="0,0 1200,0 1200,584 600,700 0,584" fill="url(#heroBase)"/>
  <polygon points="0,0 1200,0 1200,584 600,700 0,584" fill="url(#heroGlow)"/>
  <polygon points="0,0 1200,0 1200,584 600,700 0,584" fill="url(#heroWarm)"/>
</svg>
<h1 class="abs hero-title">Innovative <b>EPM</b><br><b>Solutions</b> for<br>Finance and Beyond</h1>
<p class="abs hero-lead">Brindlecrest Consulting provides decades of experience implementing Corvane EPM products with unique and innovative solutions to challenging business...</p>
<div class="btn" style="left:152px;top:490px;width:170px;height:48px;font-size:15px"><span>Learn More</span></div>
<div class="abs dot" style="left:141px"></div>
<div class="abs dot" style="left:161px"></div>
<div class="abs dot on" style="left:181px"></div>
<div class="abs dot" style="left:201px"></div>
<div class="abs dot" style="left:221px"></div>

<!-- why choose -->
<section>
  <h2 class="abs why-title"><b>Why Choose</b> Us?</h2>
  <div class="abs why-rule"></div>
  <p class="abs why-text">Brindlecrest Consulting was founded on the principles of innovation and teamwork. We innovate the products we implement through a combination of functional experience and technical expertise. When we find limitations in the products that we implement, we see this as an opportunity and a challenge to extend those products until we meet the needs of our clients. Through this innovation we have created various tools to accelerate our implementations.</p>
  <div class="btn" style="left:152px;top:1206px;width:170px;height:56px;font-size:15px"><span>Learn More</span></div>
  <div class="abs why-shadow"></div>
  <div class="abs why-art" role="img" aria-label="Collage of business and technology imagery in blue tones"></div>
</section>

<!-- services -->
<svg class="band" style="top:1331px;height:765px" viewBox="0 0 1200 765">
  <defs><linearGradient id="svcBg" x1="0" y1="0" x2="0" y2="1"><stop offset="0" stop-color="#1e6fc4"/><stop offset=".6" stop-color="#2a83d6"/><stop offset="1" stop-color="#2d7fd4"/></linearGradient></defs>
  <polygon points="0,111 784,0 1200,95 1200,765 0,765" fill="url(#svcBg)"/>
</svg>
<div class="section-title" style="top:1455px;font-size:38px;font-weight:300;color:#fff">Our Services</div>
<svg class="divider" style="top:1514px" viewBox="0 0 90 14"><line x1="0" y1="5" x2="34" y2="5" stroke="#fff" stroke-width="1.5"/><line x1="0" y1="9" x2="34" y2="9" stroke="#fff" stroke-width="1.5"/><line x1="56" y1="5" x2="90" y2="5" stroke="#fff" stroke-width="1.5"/><line x1="56" y1="9" x2="90" y2="9" stroke="#fff" stroke-width="1.5"/><circle cx="45" cy="7" r="6" fill="#fff"/></svg>

<div class="svc-card" style="left:91px">
  <div class="svc-img" role="img" aria-label="Hand holding a glowing digital globe" style="background:radial-gradient(circle at 50% 45%,#6fb6f0 0%,transparent 40%),linear-gradient(160deg,#08162a,#1c4f86 55%,#0b1c33)"></div>
  <div class="svc-icon"><svg width="28" height="28" viewBox="0 0 28 28" fill="none" stroke="#1b75bc" stroke-width="2"><rect x="5" y="4" width="18" height="20" rx="2"/><line x1="9" y1="10" x2="19" y2="10"/><line x1="9" y1="15" x2="19" y2="15"/><line x1="9" y1="20" x2="15" y2="20"/></svg></div>
  <h3>Budgeting and Forecasting</h3>
  <p>Brindlecrest specializes in both cloud and on-premise EPM solutions provided by Corvane.</p>
  <div class="svc-arrow"><svg width="14" height="14" viewBox="0 0 14 14" fill="none" stroke="#fff" stroke-width="2"><path d="M7 2v9M3 7l4 4 4-4"/></svg></div>
</div>
<div class="svc-card" style="left:350px">
  <div class="svc-img" role="img" aria-label="Business figures connected across a network" style="background:radial-gradient(circle at 55% 35%,#5a8fc4 0%,transparent 45%),linear-gradient(170deg,#141c2a,#2b3c55 55%,#0b121e)"></div>
  <div class="svc-icon"><svg width="28" height="28" viewBox="0 0 28 28" fill="none" stroke="#1b75bc" stroke-width="2"><rect x="4" y="4" width="9" height="9"/><rect x="15" y="4" width="9" height="9"/><rect x="4" y="15" width="9" height="9"/><rect x="15" y="15" width="9" height="9"/></svg></div>
  <h3>Close and Consolidation</h3>
  <p>Brindlecrest specializes in both cloud and on-premise EPM solutions provided by Corvane.</p>
  <div class="svc-arrow"><svg width="14" height="14" viewBox="0 0 14 14" fill="none" stroke="#fff" stroke-width="2"><path d="M7 2v9M3 7l4 4 4-4"/></svg></div>
</div>
<div class="svc-card" style="left:610px">
  <div class="svc-img" role="img" aria-label="Hand touching a digital analytics display" style="background:radial-gradient(circle at 55% 60%,#4a9ad8 0%,transparent 42%),linear-gradient(160deg,#1a2433,#3a4a60 50%,#0e1622)"></div>
  <div class="svc-icon"><svg width="28" height="28" viewBox="0 0 28 28" fill="none" stroke="#1b75bc" stroke-width="2"><circle cx="12" cy="12" r="7"/><line x1="17" y1="17" x2="24" y2="24"/></svg></div>
  <h3>Reporting and Analysis</h3>
  <p>Traditionally, Halcyon Planning and the Corvane EPM stack were products closely associated</p>
  <div class="svc-arrow"><svg width="14" height="14" viewBox="0 0 14 14" fill="none" stroke="#fff" stroke-width="2"><path d="M7 2v9M3 7l4 4 4-4"/></svg></div>
</div>
<div class="svc-card" style="left:869px">
  <div class="svc-img" role="img" aria-label="Businessman with glowing support network graphic" style="background:radial-gradient(circle at 60% 40%,#7cc0f5 0%,transparent 35%),radial-gradient(circle at 45% 75%,#e08a3a 0%,transparent 30%),linear-gradient(160deg,#0a1a30,#1e4a7a 55%,#0b1c33)"></div>
  <div class="svc-icon"><svg width="28" height="28" viewBox="0 0 28 28" fill="none" stroke="#1b75bc" stroke-width="2"><circle cx="14" cy="14" r="9"/><circle cx="14" cy="14" r="4"/></svg></div>
  <h3>Support Services</h3>
  <p>Lorem Ipsum is simply dummy text of the printing and typesetting industry. Lorem Ipsum</p>
  <div class="svc-arrow"><svg width="14" height="14" viewBox="0 0 14 14" fill="none" stroke="#fff" stroke-width="2"><path d="M7 2v9M3 7l4 4 4-4"/></svg></div>
</div>
<div class="abs join-circle"></div>

<!-- core values -->
<div class="section-title values-title">Our Core Values<br>Provide Our Foundation</div>
<div class="abs values-rule"></div>

<svg class="abs core-ring" viewBox="0 0 278 278"><path d="M139 4 A135 135 0 1 0 274 139" fill="none" stroke="#1b75bc" stroke-width="4"/><path d="M180 10 A135 135 0 0 1 268 100" fill="none" stroke="#1b75bc" stroke-width="4"/></svg>
<div class="abs core-disc">BRINDLECREST</div>

<div class="value left" style="left:128px;top:2340px"><h4>Clients First</h4><p>Always do the right thing for the client, no exceptions</p></div>
<svg class="value-icon" style="left:373px;top:2350px" viewBox="0 0 60 60" fill="none" stroke="#1b75bc" stroke-width="2"><circle cx="14" cy="12" r="5"/><circle cx="30" cy="10" r="5"/><circle cx="46" cy="12" r="5"/><path d="M8 44l14-14 10 6 10-8 12 14M20 50l10-8"/></svg>
<div class="value left" style="left:128px;top:2490px"><h4>Innovation</h4><p>Never satisfied with product limitations, we always find a way</p></div>
<svg class="value-icon" style="left:373px;top:2500px" viewBox="0 0 60 60" fill="none" stroke="#1b75bc" stroke-width="2"><circle cx="34" cy="18" r="11"/><path d="M29 30h10v6H29zM6 48h14l10-6h16"/></svg>

<div class="value" style="left:853px;top:2340px"><h4>Integrity</h4><p>Always do the right thing for the client, no exceptions</p></div>
<svg class="value-icon" style="left:776px;top:2350px" viewBox="0 0 60 60" fill="none" stroke="#1b75bc" stroke-width="2"><rect x="4" y="4" width="8" height="6"/><rect x="4" y="14" width="8" height="6"/><line x1="16" y1="7" x2="32" y2="7"/><line x1="16" y1="17" x2="32" y2="17"/><path d="M6 54V36h10v18M22 54V30l14-10 8 6v28"/></svg>
<div class="value" style="left:853px;top:2498px"><h4>Teamwork</h4><p>Always do the right thing for the client, no exceptions</p></div>
<svg class="value-icon" style="left:776px;top:2506px" viewBox="0 0 60 60" fill="none" stroke="#1b75bc" stroke-width="2"><circle cx="30" cy="30" r="12"/><circle cx="10" cy="10" r="5"/><circle cx="50" cy="10" r="5"/><circle cx="10" cy="50" r="5"/><circle cx="50" cy="50" r="5"/><path d="M14 14l7 7M46 14l-7 7M14 46l7-7M46 46l-7-7"/></svg>

<!-- case studies -->
<svg class="band" style="top:2690px;height:708px" viewBox="0 0 1200 708" role="img" aria-label="Blue-tinted office background">
  <defs>
    <linearGradient id="caseBg" x1="0" y1="0" x2="0" y2="1"><stop offset="0" stop-color="#1c6dc2"/><stop offset=".45" stop-color="#2b80d4"/><stop offset="1" stop-color="#1a65b6"/></linearGradient>
    <radialGradient id="caseGlow" cx=".75" cy=".25" r=".35"><stop offset="0" stop-color="#5aa5ea" stop-opacity=".6"/><stop offset="1" stop-color="#5aa5ea" stop-opacity="0"/></radialGradient>
  </defs>
  <polygon points="0,0 1200,0 1200,600 416,708 0,600" fill="url(#caseBg)"/>
  <polygon points="0,0 1200,0 1200,600 416,708 0,600" fill="url(#caseGlow)"/>
</svg>
<div class="section-title" style="top:2753px;font-size:38px;font-weight:400;color:#fff">Case Studies</div>
<svg class="divider" style="top:2812px" viewBox="0 0 90 14"><line x1="0" y1="5" x2="34" y2="5" stroke="#fff" stroke-width="1.5"/><line x1="0" y1="9" x2="34" y2="9" stroke="#fff" stroke-width="1.5"/><line x1="56" y1="5" x2="90" y2="5" stroke="#fff" stroke-width="1.5"/><line x1="56" y1="9" x2="90" y2="9" stroke="#fff" stroke-width="1.5"/><circle cx="45" cy="7" r="6" fill="#fff"/></svg>

<div class="case-card" style="left:207px">
  <div class="case-img" role="img" aria-label="Stacked coins with a rising financial chart" style="background:radial-gradient(circle at 70% 55%,#e0783a 0%,transparent 30%),radial-gradient(circle at 35% 40%,#5aa8ee 0%,transparent 40%),linear-gradient(135deg,#0b1730,#2466b0 55%,#0e1e3a)"></div>
  <h3>Lorem Ipsum is simply dummy text</h3>
  <p>Lorem Ipsum is simply dummy text of the printing and typesetting industry. Lorem Ipsum</p>
  <div class="btn"><span>Learn More</span></div>
</div>
<div class="case-card" style="left:633px">
  <div class="case-img" role="img" aria-label="Hand pointing at a digital data screen" style="background:radial-gradient(circle at 40% 60%,#3fb0c8 0%,transparent 38%),radial-gradient(circle at 85% 30%,#d99a4a 0%,transparent 25%),linear-gradient(135deg,#0a1426,#1d4f86 55%,#0b1a30)"></div>
  <h3>Lorem Ipsum is simply dummy text</h3>
  <p>Lorem Ipsum is simply dummy text of the printing and typesetting industry. Lorem Ipsum</p>
  <div class="btn"><span>Learn More</span></div>
</div>

<!-- blog -->
<div class="section-title blog-title">Recent Blog Posts</div>
<svg class="divider" style="top:3508px" viewBox="0 0 90 14"><line x1="0" y1="5" x2="34" y2="5" stroke="#6d6f71" stroke-width="1.5"/><line x1="0" y1="9" x2="34" y2="9" stroke="#6d6f71" stroke-width="1.5"/><line x1="56" y1="5" x2="90" y2="5" stroke="#6d6f71" stroke-width="1.5"/><line x1="56" y1="9" x2="90" y2="9" stroke="#6d6f71" stroke-width="1.5"/><circle cx="45" cy="7" r="6" fill="#6d6f71"/></svg>

<article class="blog-card" style="left:143px">
  <div class="blog-img" role="img" aria-label="Hands holding a newspaper beside a phone" style="background:radial-gradient(circle at 45% 45%,#e8e8e8 0%,transparent 40%),linear-gradient(135deg,#3a3a3a,#8c8c8c 50%,#2b2b2b)"></div>
  <div class="blog-date">OCT<br>2024</div>
  <div class="blog-body">
    <h3>Corvane Cloud EPM Updates – October 2022</h3>
    <div class="blog-author">Mara Velden</div>
    <p>Sed ut perspiciatis unde omnis iste natus error sit voluptatem accustium dlorue laum</p>
    <div class="btn"><span>Learn More</span></div>
  </div>
</article>
<article class="blog-card" style="left:455px">
  <div class="blog-img" role="img" aria-label="Award winners announcement with gold stars" style="background:radial-gradient(circle at 50% 45%,#c9a24a 0%,transparent 35%),linear-gradient(160deg,#0f1a3d,#27356e 60%,#0b1230)"></div>
  <div class="blog-date">OCT<br>2024</div>
  <div class="blog-body">
    <h3>Encore Webinar of Keystage22's Overall Top</h3>
    <div class="blog-author">Owen Harcourt</div>
    <p>Sed ut perspiciatis unde omnis iste natus error sit voluptatem accustium dlorue laum</p>
    <div class="btn"><span>Learn More</span></div>
  </div>
</article>
<article class="blog-card" style="left:768px">
  <div class="blog-img" role="img" aria-label="Hand over a glowing workforce analytics chart" style="background:radial-gradient(circle at 55% 55%,#6ec2f0 0%,transparent 38%),linear-gradient(150deg,#0b2340,#1f5f9c 55%,#0a1c33)"></div>
  <div class="blog-date">OCT<br>2024</div>
  <div class="blog-body">
    <h3>Workforce Planning can be Groovy</h3>
    <div class="blog-author">Lena Strand</div>
    <p>Sed ut perspiciatis unde omnis iste natus error sit voluptatem accustium dlorue laum</p>
    <div class="btn"><span>Learn More</span></div>
  </div>
</article>

<!-- quotation -->
<svg class="band" style="top:4096px;height:480px" viewBox="0 0 1200 480" role="img" aria-label="Team meeting around a wooden table with laptops and coffee">
  <defs>
    <linearGradient id="quoteBg" x1="0" y1="0" x2="1" y2=".5"><stop offset="0" stop-color="#1b1109"/><stop offset=".4" stop-color="#5a3819"/><stop offset=".75" stop-color="#33200f"/><stop offset="1" stop-color="#140d07"/></linearGradient>
    <radialGradient id="quoteGlow" cx=".55" cy=".45" r=".3"><stop offset="0" stop-color="#a06a34" stop-opacity=".6"/><stop offset="1" stop-color="#a06a34" stop-opacity="0"/></radialGradient>
  </defs>
  <polygon points="0,102 416,0 1200,102 1200,480 0,480" fill="#1b75bc"/>
  <polygon points="0,112 416,10 1200,112 1200,480 0,480" fill="url(#quoteBg)"/>
  <polygon points="0,112 416,10 1200,112 1200,480 0,480" fill="url(#quoteGlow)"/>
</svg>
<h2 class="abs quote-title">Request For Quotation</h2>
<p class="abs quote-text">Sed ut perspiciatis unde omnis iste natus voluptatem accusantium doloremque laudantium</p>
<div class="btn" style="left:152px;top:4425px;width:190px;height:48px;font-size:15px"><span>Get Started</span></div>

<!-- footer -->
<footer>
  <div class="abs footer"></div>
  <div class="abs brand foot-brand">BRINDLECREST</div>
  <div class="abs foot-sub">CONSULTING</div>
  <div class="abs social-foot" style="left:145px"></div>
  <div class="abs social-foot" style="left:187px"></div>
  <div class="abs social-foot" style="left:229px"></div>
  <div class="abs social-foot" style="left:271px"></div>

  <div class="abs foot-h" style="left:480px;top:4640px">LINKS</div>
  <div class="foot-links">
    <a style="top:4688px">Home</a>
    <a style="top:4722px">About us</a>
    <a style="top:4756px">Services</a>
    <a style="top:4790px">Blog</a>
    <a style="top:4824px">Case Studies</a>
  </div>

  <div class="abs foot-h" style="left:755px;top:4638px">SIGN UP TO RECEIVE EMAIL</div>
  <div class="abs foot-note">Excepteur sint occaecat cupidatat non proident, sunt in culpa qui Nemo enim ipsam</div>
  <div class="abs foot-input">Enter Email</div>
  <div class="btn" style="left:762px;top:4808px;width:122px;height:34px;font-size:11px"><span>Subscribe</span></div>

  <div class="abs copyright">Copyright © Brindlecrest Consultig 2024. All rights reserved. | Privacy Policy</div>
</footer>

</body>
</html>
```